KerrLow Farm

Need a nice simple clean double sided business card that has our logo and info on:
Kerr Low Farm
Martin & Felicity Kerr Low
kerrlowfarm@mailbarn.example
Martin: 1-780-555-0148
Felicity: 1-780-555-0193
Instagram @ kerrlow_farm

Contact Information for Business Card

Martin & Felicity Kerr Low kerrlowfarm@mailbarn.example Martin: 1-780-555-0148 Felicity: 1-780-555-0193

```html
<!DOCTYPE html>
<html lang="en">
<head>
<meta charset="utf-8">
<title>Kerr Low Farm – Business Card</title>
<link rel="stylesheet" href="https://fonts.googleapis.com/css2?family=Montserrat:wght@500;600;700&display=swap">
<style>
  :root {
    --backdrop: #b4b4b4;
    --leaf: #68a343;
    --leaf-back: #5e9e46;
    --harvest: #f6a01c;
    --paper: #ffffff;
  }
  * { margin: 0; padding: 0; box-sizing: border-box; }
  html, body {
    width: 1200px; height: 1200px; overflow: hidden;
    background: var(--backdrop);
    font-family: "Montserrat", sans-serif;
  }
  .card {
    position: absolute;
    left: 228px;
    width: 746px;
    height: 427px;
    overflow: hidden;
  }
  .card--front { top: 113px; background: var(--paper); }
  .card--back { top: 583px; background: var(--leaf-back); }

  .wave { position: absolute; inset: 0; width: 100%; height: 100%; }

  .brand-mark {
    position: absolute;
    left: 473px; top: 30px;
    width: 200px;
    text-align: center;
  }
  .brand-mark__ring {
    display: block;
    margin: 0 auto;
    width: 100px; height: 100px;
    border: 3px solid var(--leaf);
    border-radius: 50%;
  }
  .brand-mark__name {
    margin-top: 12px;
    font-size: 24px;
    font-weight: 600;
    color: var(--leaf);
    white-space: nowrap;
    margin-left: -40px; margin-right: -40px;
  }

  .contact { position: absolute; left: 26px; top: 226px; color: var(--paper); }
  .contact__farm {
    font-size: 24px; font-weight: 700; color: var(--harvest);
    letter-spacing: 0.2px;
  }
  .contact__people {
    margin-top: 16px;
    font-size: 18px; font-weight: 700;
  }
  .contact__rule {
    width: 31px; height: 4px; background: var(--harvest);
    margin: 9px 0 14px 1px;
  }
  .contact__list { list-style: none; }
  .contact__item {
    display: flex; align-items: center; gap: 12px;
    font-size: 17.5px; font-weight: 500;
    height: 29.5px;
  }
  .contact__icon { width: 18px; height: 18px; flex: none; fill: var(--paper); }

  .back-mark {
    position: absolute; left: 0; right: 0; top: 106px;
    text-align: center; color: var(--paper);
  }
  .back-mark__ring {
    display: block; margin: 0 auto;
    width: 148px; height: 148px;
    border: 4px solid var(--paper);
    border-radius: 50%;
  }
  .back-mark__name {
    margin-top: 22px;
    font-size: 38px; font-weight: 500;
    letter-spacing: 0.5px;
  }
</style>
</head>
<body>

<section class="card card--front">
  <svg class="wave" viewBox="0 0 1200 688" preserveAspectRatio="none" aria-hidden="true">
    <path fill="var(--harvest)" d="M40,252 C100,190 160,167 230,167 C450,167 800,440 1010,440 C1100,440 1165,400 1200,348 L1200,688 L0,688 L0,300 Z"/>
    <path fill="var(--paper)" d="M0,298 C60,216 140,182 215,184 C440,188 800,455 1010,455 C1100,455 1165,412 1200,364 L1200,688 L0,688 Z"/>
    <path fill="var(--leaf)" d="M0,310 C60,232 130,197 210,199 C430,203 800,465 1010,465 C1100,465 1165,424 1200,378 L1200,688 L0,688 Z"/>
  </svg>

  <div class="brand-mark">
    <span class="brand-mark__ring"></span>
    <p class="brand-mark__name">KERR LOW FARM</p>
  </div>

  <div class="contact">
    <h1 class="contact__farm">KERR LOW FARM</h1>
    <p class="contact__people">MARTIN &amp; FELICITY KERR LOW</p>
    <div class="contact__rule"></div>
    <ul class="contact__list">
      <li class="contact__item">
        <svg class="contact__icon" viewBox="0 0 24 24" aria-hidden="true"><path d="M6.6 10.8a15.1 15.1 0 0 0 6.6 6.6l2.2-2.2a1 1 0 0 1 1-.25 11.4 11.4 0 0 0 3.6.57 1 1 0 0 1 1 1V20a1 1 0 0 1-1 1A17 17 0 0 1 3 4a1 1 0 0 1 1-1h3.5a1 1 0 0 1 1 1c0 1.25.2 2.45.57 3.6a1 1 0 0 1-.25 1z"/></svg>
        kerrlowfarm@mailbarn.example
      </li>
      <li class="contact__item">
        <svg class="contact__icon" viewBox="0 0 24 24" aria-hidden="true"><path d="M2 5h20v14H2z M2 5l10 7 10-7" fill="var(--paper)"/><path d="M2 5l10 7 10-7" fill="none" stroke="var(--leaf)" stroke-width="1.6"/></svg>
        Martin: 1-780-555-0148
      </li>
      <li class="contact__item">
        <svg class="contact__icon" viewBox="0 0 24 24" aria-hidden="true"><circle cx="12" cy="12" r="10"/><path d="M7 7c2 0 3 1 3 3s-2 2-2 4 1 3 0 5M15 4c0 2 2 2 3 4s-2 3-1 5 2 2 3 2" fill="none" stroke="var(--leaf)" stroke-width="1.6"/></svg>
        Felicity: 1-780-555-0193
      </li>
    </ul>
  </div>
</section>

<section class="card card--back">
  <div class="back-mark">
    <span class="back-mark__ring"></span>
    <p class="back-mark__name">KERR LOW FARM</p>
  </div>
</section>

</body>
</html>
```